Pinecrest Haulers ~ A+ Division of Vantor

Energetic ,different ,exotic ,modern,
never before done, next level buisness card for a trash dumpster company
is for a trash removal construction company ...please have your wildest ideas i dont want a boring basic buisness card i want people to say wow !! And be able to mention you and who designed my card ...i know you take pride in your work i do to ....3 years ago quillwork from brief hive made a logo for me and i still love it .....use his colors and the word vantor DO NOT USE ROOFING AND REMODELING use Pinecrest Haulers ....look at his Logo i Like the [S] LOGO and word Vantor ....you surprise me and we will do alot more projects with you and or brief hive ....thank you for your hard work and your time i do appreciate all of you and admire your skills designing .....i really do appreciate all of you thank you -todd
Ps Lets make these biz cards special different from many ,unique

Target Market(s)

Construction .....dumpsters trash Trash removal

Industry/Entity Type

Construction

Contact Information for Business Card

Black gold white maybe more colors

Requirements
Must have
• Vantor ~Pinecrest Haulers division Serving Atlanta and surrounding areas'Chief executive Todd Marlow cell 404 555 0147 Office 404 888 8888Follow us on fb ,instagram .. email Pinecresthaulers-demo.com Hablamos espaƱol
Nice to have
• Black gold white colors like my logo i updated and you can add more if you want ....its a construction / trucking company dumpster Trash company we recycle also
Should not have
• When you look at my logo (Must not have roofing and remodeling )

```html
<!DOCTYPE html>
<html lang="en">
<head>
<meta charset="utf-8">
<title>Vantor · Pinecrest Haulers business card</title>
<link rel="stylesheet" href="https://fonts.googleapis.com/css2?family=Open+Sans:wght@400;600;800&family=Titillium+Web:wght@600&family=Tinos&display=swap">
<style>
  :root {
    --backdrop: #a3a3a3;
    --card-white: #ffffff;
    --gold: #e3b422;
    --gold-deep: #d9a81a;
    --ink: #1e1e1e;
    --charcoal: #262626;
    --rule: #8a8a8a;
    --social: #4a5a7a;
  }
  * { margin: 0; padding: 0; box-sizing: border-box; }
  html, body { width: 1200px; height: 900px; overflow: hidden; }
  body {
    background: var(--backdrop);
    position: relative;
    font-family: "Open Sans", Arial, sans-serif;
    color: var(--ink);
  }
  .card {
    position: absolute;
    top: 306px;
    height: 272px;
    box-shadow: 3px 4px 6px rgba(0,0,0,0.35);
    overflow: hidden;
  }
  .card--front { left: 150px; width: 438px; background: var(--card-white); }
  .card--back { left: 608px; width: 441px; height: 273px; background: var(--charcoal); }

  /* front */
  .brand { position: absolute; left: 40px; top: 84px; width: 175px; text-align: center; }
  .brand__mark {
    width: 59px; height: 59px; margin: 0 auto;
    background: linear-gradient(135deg, #f1c63a, var(--gold-deep));
  }
  .brand__name {
    margin-top: 10px;
    font-weight: 800; font-size: 27px; letter-spacing: 0.5px; line-height: 1;
    color: var(--ink);
  }
  .brand__division {
    margin-top: 4px;
    font-weight: 600; font-size: 6.5px; letter-spacing: 3.2px;
    color: var(--gold); text-transform: uppercase;
  }
  .divider { position: absolute; left: 231px; top: 68px; width: 1px; height: 131px; background: var(--rule); }

  .contact { position: absolute; left: 246px; top: 62px; }
  .contact__name {
    font-family: "Titillium Web", "Open Sans", sans-serif;
    font-weight: 600; font-size: 19px; line-height: 1; color: var(--gold);
    text-transform: uppercase;
  }
  .contact__title { font-size: 11.5px; margin-top: 2px; }
  .contact__list { list-style: none; margin-top: 22px; }
  .contact__item { display: flex; align-items: center; font-size: 12px; line-height: 15.5px; }
  .contact__icon { width: 10px; height: 10px; margin: 0 6px 0 2px; flex: none; }
  .contact__follow { display: flex; align-items: center; margin-top: 14px; font-size: 12px; }
  .contact__social { width: 15px; height: 15px; background: var(--social); margin-left: 4px; }

  .band {
    position: absolute; left: 0; bottom: 0; width: 100%; height: 53px;
    background: var(--gold-deep);
    display: flex; align-items: center; justify-content: center;
    font-weight: 600; font-size: 11.5px; color: var(--ink);
  }

  /* back */
  .backdrop-pattern { position: absolute; inset: 0; background: #2b2b2b; }
  .back__mark {
    position: absolute; left: 337px; top: 111px; width: 46px; height: 46px;
    background: linear-gradient(135deg, #f1c63a, var(--gold-deep));
    border: 2px solid #1a1a1a;
  }
  .back__motto {
    position: absolute; left: 0; width: 100%; top: 203px;
    text-align: center; font-family: "Tinos", "Times New Roman", serif;
    font-size: 19px; line-height: 24px; color: var(--gold); text-transform: uppercase;
  }
</style>
</head>
<body>

<section class="card card--front">
  <div class="brand">
    <div class="brand__mark"></div>
    <div class="brand__name">VANTOR</div>
    <div class="brand__division">Pinecrest Haulers</div>
  </div>

  <div class="divider"></div>

  <div class="contact">
    <div class="contact__name">Todd Marlow</div>
    <div class="contact__title">Chief executive</div>
    <ul class="contact__list">
      <li class="contact__item">
        <svg class="contact__icon" viewBox="0 0 10 10"><rect width="10" height="10" fill="#e3b422"/><rect x="3" y="1.5" width="4" height="7" rx="0.6" fill="none" stroke="#fff" stroke-width="1"/></svg>
        404 555 0147
      </li>
      <li class="contact__item">
        <svg class="contact__icon" viewBox="0 0 10 10"><rect width="10" height="10" fill="#e3b422"/><path d="M2 4 Q5 1.5 8 4 L7 5 L3 5 Z M3 6 H7 V8 H3 Z" fill="#fff"/></svg>
        404 555 0162
      </li>
      <li class="contact__item">
        <svg class="contact__icon" viewBox="0 0 10 10"><rect width="10" height="10" fill="#e3b422"/><rect x="2" y="3" width="6" height="4" fill="none" stroke="#fff" stroke-width="0.9"/><path d="M2 3 L5 5.3 L8 3" fill="none" stroke="#fff" stroke-width="0.9"/></svg>
        info@pinecresthaulers-demo.com
      </li>
      <li class="contact__item">
        <svg class="contact__icon" viewBox="0 0 10 10"><rect width="10" height="10" fill="#e3b422"/><circle cx="5" cy="5" r="2.8" fill="none" stroke="#fff" stroke-width="0.9"/><path d="M2.2 5 H7.8" stroke="#fff" stroke-width="0.7"/></svg>
        www.pinecresthaulers-demo.com
      </li>
    </ul>
    <div class="contact__follow">
      Follow us on
      <span class="contact__social" aria-hidden="true"></span>
      <span class="contact__social" aria-hidden="true"></span>
    </div>
  </div>

  <div class="band">SERVING ATLANTA AND SURROUNDING AREAS</div>
</section>

<section class="card card--back">
  <div class="backdrop-pattern" role="img" aria-label="Dark tiled background of faint repeated brand squares"></div>
  <div class="back__mark"></div>
  <p class="back__motto">Life begins at the end of<br>your comfort zone</p>
</section>

</body>
</html>
```